Corvane Electrical Solutions

On one side. LOGO (underneath:) Commercial Industrial Residential

- NAME & CONTACT DETAILS

Marcus T. Hollings
Project Manager

(Cell icon) (441) 582-6197
(Email icon) cvnelectricalsoultions@mailventra.com
(Facebook & Instagram icons )@cvnelectricalsolutions

Other side: LOGO - underneath ELECTRICAL CONSTRUCTION & MAINTENANCE . LED LIGHTING & AUTOMATION . LIFE SAFETY SYSTEMS (FIRE ALARM / SECURITY) . DATA & COMMUNICATION

```html
<!DOCTYPE html>
<html lang="en">
<head>
<meta charset="utf-8">
<title>Corvane Electrical Solutions – Business Card</title>
<link href="https://fonts.googleapis.com/css2?family=Arimo:wght@400;700&family=Montserrat:wght@500&display=swap" rel="stylesheet">
<style>
  :root {
    --backdrop: #161616;
    --card: #2a292a;
    --logo-tone: #6e6e6e;
    --text-tone: #9a9a9a;
    --name-tone: #a8a8a8;
    --rule: #5c5c5c;
  }
  * { margin: 0; padding: 0; box-sizing: border-box; }
  html, body {
    width: 1200px; height: 900px; overflow: hidden;
    background: var(--backdrop);
  }
  .sheet {
    width: 1200px; height: 900px;
    display: flex; flex-direction: column; align-items: center; justify-content: center;
    gap: 36px;
  }
  .card {
    width: 740px; height: 405px;
    background: var(--card);
    position: relative;
    box-shadow: 0 6px 18px rgba(0,0,0,.5);
  }

  /* Front */
  .card--front .brand {
    position: absolute; left: 0; right: 0; top: 130px;
    display: flex; justify-content: center; align-items: center; gap: 18px;
  }
  .brand-mark {
    width: 34px; height: 34px; background: var(--logo-tone);
  }
  .brand-name {
    font-family: "Montserrat", sans-serif; font-weight: 500;
    color: var(--logo-tone); text-transform: uppercase; letter-spacing: 4px;
    line-height: 1.12;
  }
  .card--front .brand-name { font-size: 30px; }
  .services {
    position: absolute; left: 0; right: 0; top: 262px;
    font-family: "Arimo", sans-serif; font-size: 13.5px; letter-spacing: .6px;
    color: var(--text-tone); text-transform: uppercase; text-align: center; line-height: 1.35;
  }

  /* Back */
  .card--back .identity {
    position: absolute; left: 48px; top: 145px; width: 300px;
  }
  .card--back .brand { display: flex; align-items: center; gap: 12px; }
  .card--back .brand-mark { width: 22px; height: 22px; }
  .card--back .brand-name { font-size: 15.5px; letter-spacing: 2.2px; }
  .sectors {
    margin-top: 14px;
    font-family: "Arimo", sans-serif; font-size: 13.5px; letter-spacing: .5px;
    color: var(--logo-tone); text-transform: uppercase;
  }
  .divider {
    position: absolute; left: 382px; top: 110px; width: 1.5px; height: 185px;
    background: var(--rule);
  }
  .person {
    position: absolute; left: 410px; top: 118px;
    font-family: "Arimo", sans-serif;
  }
  .person-name { font-size: 24px; font-weight: 700; color: var(--name-tone); letter-spacing: .5px; }
  .person-role { font-size: 16px; color: var(--text-tone); margin-top: 2px; }
  .contacts { list-style: none; margin-top: 22px; }
  .contacts li {
    display: flex; align-items: center; gap: 14px;
    font-size: 15px; color: var(--text-tone); height: 27px;
  }
  .contacts svg { width: 17px; height: 17px; flex: none; }
  .social-dots { display: flex; gap: 5px; }
  .social-dot { width: 14px; height: 14px; border: 1.5px solid var(--text-tone); border-radius: 50%; }
</style>
</head>
<body>
<main class="sheet">

  <section class="card card--front" aria-label="Card front">
    <div class="brand">
      <span class="brand-mark"></span>
      <span class="brand-name">Corvane<br>Electrical<br>Solutions</span>
    </div>
    <p class="services">
      Electrical Construction &amp; Maintenance . LED Lighting &amp; Automation<br>
      Life Safety Systems (Fire Alarm / Security) . Data &amp; Communication
    </p>
  </section>

  <section class="card card--back" aria-label="Card back">
    <div class="identity">
      <div class="brand">
        <span class="brand-mark"></span>
        <span class="brand-name">Corvane<br>Electrical<br>Solutions</span>
      </div>
      <p class="sectors">Commercial Industrial Residential</p>
    </div>

    <div class="divider"></div>

    <div class="person">
      <h1 class="person-name">Marcus T. Hollings</h1>
      <p class="person-role">Project Manager</p>
      <ul class="contacts">
        <li>
          <svg viewBox="0 0 24 24" aria-hidden="true"><path fill="#9a9a9a" d="M6.6 10.8a15.1 15.1 0 0 0 6.6 6.6l2.2-2.2c.3-.3.7-.4 1-.2 1.1.4 2.3.6 3.6.6.6 0 1 .4 1 1V20c0 .6-.4 1-1 1A17 17 0 0 1 3 4c0-.6.4-1 1-1h3.5c.6 0 1 .4 1 1 0 1.3.2 2.5.6 3.6.1.3 0 .7-.2 1z"/></svg>
          (441) 582-6197
        </li>
        <li>
          <svg viewBox="0 0 24 24" aria-hidden="true"><rect x="2.5" y="5" width="19" height="14" fill="none" stroke="#9a9a9a" stroke-width="1.6"/><path d="M2.5 5l9.5 8 9.5-8M2.5 19l7-6.5M21.5 19l-7-6.5" fill="none" stroke="#9a9a9a" stroke-width="1.6"/></svg>
          cvnelectricalsoultions@mailventra.com
        </li>
        <li>
          <span class="social-dots"><span class="social-dot"></span><span class="social-dot"></span></span>
          @cvnelectricalsolutions
        </li>
      </ul>
    </div>
  </section>

</main>
</body>
</html>
```